CALMIVERA BROCHURE/CATALOG DESIGN
SPA AND WELLNESS CENTRE
We need a new design for our brochure/catalogue. This is related to spa industry. We have over 10 locations and expanding. We need the design to be modern and must resemble some parts of our logo design as well.
for services and price list:
http://www.calmiverahealth.example/services_massage.php
For locations:
http://www.calmiverahealth.example/locations.php
Must say somewhere in services and prices:
1) Please speak to our receptionist for any insurance related questions. (or something similar)
2) Gift Certificates Available and redeemable at any of our locations.
3) Package Card Available and usable at any of our locations.
#2 and #3 can be used in a paragraph form in our about us section.
Also please include out website:
www.calmiverahealth.example
Salon & Spa
Corporate/family/fun/personal/wellness/female/male/any age
Must be modern!
Must resemble the spa/wellness industry type design!
Must have all our services and prices!
Must be easy to read our services and prices!
We suggest the brochure to have following:
About Calmivera
Services and Prices
Locations
We think in order to fit all servies and prices and about us info, may be ok to use 4 page layout for brochure design.

```html
<!DOCTYPE html>
<html lang="en">
<head>
<meta charset="utf-8">
<title>Calmivera Brochure – Outside</title>
<link href="https://fonts.googleapis.com/css2?family=Great+Vibes&family=Open+Sans:wght@400;600;700&display=swap" rel="stylesheet">
<style>
:root{
  --board:#0d1f4a;
  --board-light:#1c3b7a;
  --sky:#2aa7de;
  --sky-deep:#1477b8;
  --cyan:#7fe3ff;
  --leaf:#7cbf2f;
  --leaf-deep:#3f8a1c;
  --lime:#c9e46a;
  --ink:#2b3a44;
  --muted:#5d6b73;
  --paper:#f4f9f6;
  --white:#ffffff;
}
*{box-sizing:border-box;margin:0;padding:0}
html,body{width:1200px;height:872px;overflow:hidden}
body{background:radial-gradient(ellipse at 50% 40%,var(--board-light),var(--board) 75%);font-family:"Open Sans",Arial,sans-serif;color:var(--ink);position:relative}
.board-label{position:absolute;color:var(--white);font-size:22px;font-weight:600;letter-spacing:.5px}
.label-outside{top:14px;left:0;width:1200px;text-align:center;font-size:26px}
.label-back{top:838px;left:130px}
.label-front{top:838px;left:1016px}
.brochure{position:absolute;left:54px;top:58px;width:1092px;height:762px;display:flex;box-shadow:0 6px 24px rgba(0,0,0,.5);overflow:hidden}
.panel{position:relative;height:100%;overflow:hidden}
.script{font-family:"Great Vibes",cursive;font-weight:400}

/* Locations */
.panel-locations{width:332px;background:linear-gradient(180deg,var(--sky-deep) 0%,var(--sky) 45%,#63c3ea 75%,#9bd6e6 100%);color:var(--white)}
.storefront{position:absolute;left:10px;top:10px;width:112px;height:110px;background:linear-gradient(160deg,#5a6f7d,#2f3c46 60%,#8a6a44);border:2px solid rgba(255,255,255,.6)}
.panel-locations .title{position:absolute;left:134px;top:2px;font-size:58px;color:var(--white)}
.panel-locations .tagline{position:absolute;left:146px;top:72px;width:170px;font-size:15px;font-weight:700;color:var(--cyan);line-height:1.2}
.loc-grid{position:absolute;left:12px;top:134px;width:310px;display:grid;grid-template-columns:1fr 1fr;column-gap:12px;row-gap:9px}
.loc h4{font-size:8px;font-weight:700;color:var(--cyan)}
.loc p{font-size:7px;line-height:1.3;color:var(--white)}
.soon{position:absolute;left:14px;top:560px;font-size:50px;color:var(--white)}
.loc-soon{position:absolute;left:12px;top:640px;width:310px;display:grid;grid-template-columns:1fr 1fr;column-gap:12px}
.leaf-fade{position:absolute;left:0;bottom:0;width:332px;height:110px;background:linear-gradient(180deg,rgba(155,214,230,0),rgba(124,191,47,.55))}

/* About */
.panel-about{width:296px;background:var(--paper)}
.about-sky{position:absolute;left:0;top:0;width:296px;height:150px;background:linear-gradient(180deg,#3fa9dc,#a9dbef 60%,var(--paper))}
.panel-about .title{position:absolute;left:12px;top:2px;font-size:58px;color:var(--white)}
.drops{position:absolute;right:0;top:0;width:120px;height:150px;background:radial-gradient(circle at 60% 40%,#cfeefa,#5fb6de 70%,rgba(95,182,222,0))}
.section-head{display:flex;align-items:center;gap:8px;font-size:13px;font-weight:700;color:var(--sky-deep)}
.what-we-do{position:absolute;left:26px;top:170px;width:250px}
.what-expect{position:absolute;left:26px;top:400px;width:250px}
.body-copy{margin-top:10px;font-size:9.5px;line-height:1.45;color:var(--muted);padding-left:22px}
.body-copy .drop{float:left;font-family:"Great Vibes",cursive;font-size:34px;line-height:.9;color:var(--sky-deep);margin-right:3px}
.gift{position:absolute;left:70px;top:640px;width:210px;padding:10px 12px;border:1px solid var(--leaf);background:rgba(124,191,47,.12);font-size:10px;line-height:1.4;color:var(--leaf-deep);font-weight:600;text-align:center}

/* Packages */
.panel-packages{width:194px;background:var(--white)}
.pkg-top{position:absolute;left:0;top:0;width:194px;height:140px;background:linear-gradient(180deg,#d8ec8a,#f1f8d6 70%,var(--white))}
.panel-packages .title{position:absolute;left:12px;top:4px;font-size:52px;color:var(--white);text-shadow:0 0 1px rgba(63,138,28,.4)}
.pkg-heading{position:absolute;left:8px;display:flex;align-items:center;gap:5px;font-size:12px;font-weight:700;color:var(--leaf-deep)}
.pkg-list{position:absolute;left:30px;width:156px}
.pkg{margin-bottom:6px;background:#f3f9e8}
.pkg h5{background:var(--leaf);color:var(--white);font-size:7.5px;font-weight:700;padding:2px 4px}
.pkg p{font-size:6.5px;line-height:1.35;color:var(--muted);padding:2px 4px}
.pkg .price{font-weight:700;color:var(--ink)}
.pkg-bottom{position:absolute;left:0;bottom:0;width:194px;height:80px;background:linear-gradient(180deg,rgba(201,228,106,0),#c9e46a)}

/* Front */
.panel-front{width:270px;background:linear-gradient(170deg,#b9dd5c 0%,#6fb52e 40%,#3f8a1c 75%,#2c6a14 100%)}
.front-photo{position:absolute;inset:0;background:radial-gradient(ellipse at 40% 45%,rgba(255,255,255,.35),rgba(255,255,255,0) 55%)}
.brand{position:absolute;right:14px;top:14px;display:flex;align-items:center;gap:6px;color:var(--white);font-size:15px;font-weight:700;letter-spacing:1px}
.brand .dot{width:24px;height:24px;border-radius:50%;background:var(--sky-deep)}
.slogan{position:absolute;left:70px;top:370px;width:190px;font-size:40px;line-height:.95;color:var(--white);text-align:center;transform:rotate(-8deg)}
.web{position:absolute;left:0;bottom:14px;width:260px;text-align:right;font-size:11px;font-weight:700;color:var(--white)}
</style>
</head>
<body>
<div class="board-label label-outside">Outside</div>

<main class="brochure">
  <section class="panel panel-locations">
    <div class="storefront" role="img" aria-label="Photo of a Calmivera spa storefront"></div>
    <h2 class="title script">Locations</h2>
    <p class="tagline">Come and visit us on our branches</p>
    <div class="loc-grid">
      <div class="loc"><h4>Main</h4><p>1200 Harbour Blvd, Unit 4<br>Lakeport, ON L1A 2B3<br>T: (555) 010-2201<br>Mon to Sat 10am to 9pm</p></div>
      <div class="loc"><h4>Northfield Location</h4><p>88 Maple Street, Unit 2<br>Northfield, ON N2B 3C4<br>T: (555) 010-2202<br>Mon to Sat 10am to 8pm</p></div>
      <div class="loc"><h4>Harrowmere Location</h4><p>415 Queen Road, Unit 9<br>Harrowmere, ON H3C 4D5<br>T: (555) 010-2203<br>Mon to Sun 10am to 8pm</p></div>
      <div class="loc"><h4>Elmsbrook Location</h4><p>27 Willow Lane, Suite 5<br>Elmsbrook, ON E4D 5F6<br>T: (555) 010-2204<br>Mon to Sat 9am to 8pm</p></div>
      <div class="loc"><h4>Cedarvale Location</h4><p>930 Brook Avenue<br>Cedarvale, ON C5E 6G7<br>T: (555) 010-2205<br>Mon to Fri 10am to 9pm</p></div>
      <div class="loc"><h4>Ridgeton Location</h4><p>16 Pine Crescent, Unit 1<br>Ridgeton, ON R6F 7H8<br>T: (555) 010-2206<br>Mon to Sat 10am to 7pm</p></div>
      <div class="loc"><h4>Westgate Centre</h4><p>3300 Westgate Road<br>Lakeport, ON L7G 8J9<br>T: (555) 010-2207<br>Mon to Sun 10am to 9pm</p></div>
      <div class="loc"><h4>Southpoint Location</h4><p>71 Orchard Way, Unit 3<br>Southpoint, ON S8H 9K1<br>T: (555) 010-2208<br>Mon to Sat 10am to 8pm</p></div>
      <div class="loc"><h4>Fairhill Location</h4><p>540 Station Street<br>Fairhill, ON F9J 1L2<br>T: (555) 010-2209<br>Mon to Sat 10am to 8pm</p></div>
      <div class="loc"><h4>Bayside Location</h4><p>12 Shoreline Drive<br>Bayside, ON B1K 2M3<br>T: (555) 010-2210<br>Mon to Sun 11am to 7pm</p></div>
    </div>
    <h2 class="soon script">Soon to Open</h2>
    <div class="loc-soon">
      <div class="loc"><h4>Eastmoor Location</h4><p>205 Garden Road<br>Eastmoor, ON E2L 3N4<br>T: (555) 010-2211</p></div>
      <div class="loc"><h4>Millbrook Location</h4><p>64 River Street<br>Millbrook, ON M3M 4P5<br>T: (555) 010-2212</p></div>
    </div>
    <div class="leaf-fade" role="img" aria-label="Soft photo of green leaves fading in"></div>
  </section>

  <section class="panel panel-about">
    <div class="about-sky"></div>
    <div class="drops" role="img" aria-label="Photo of water droplets"></div>
    <h2 class="title script">About Us</h2>
    <div class="what-we-do">
      <h3 class="section-head"><svg width="16" height="16" viewBox="0 0 16 16"><circle cx="8" cy="8" r="6" fill="none" stroke="#1477b8" stroke-width="2"/></svg>What we do</h3>
      <p class="body-copy"><span class="drop">D</span>edicated to helping you relieve stress, reduce tension, manage pain and help you reach an overall sense of well-being. Since 1999 people have come to our spas seeking a relaxing and rejuvenating experience. We work with each client on an individual basis to establish their specific needs and then meet those needs through a thorough and nurturing treatment.</p>
    </div>
    <div class="what-expect">
      <h3 class="section-head"><svg width="16" height="16" viewBox="0 0 16 16"><circle cx="8" cy="8" r="6" fill="none" stroke="#1477b8" stroke-width="2"/></svg>What to expect at Calmivera</h3>
      <p class="body-copy"><span class="drop">O</span>ur receptionists are friendly and highly qualified to provide the best customer service and to focus on answering any questions or concerns our clients may have, including insurance. Our therapists are trained in both traditional and modern techniques, ensuring you will be 100% satisfied with any of the services we offer.</p>
    </div>
    <p class="gift">Gift Certificates and Package Cards are available and redeemable at any of our locations.</p>
  </section>

  <section class="panel panel-packages">
    <div class="pkg-top" role="img" aria-label="Photo of fresh green leaves"></div>
    <h2 class="title script">Packages</h2>
    <h3 class="pkg-heading" style="top:120px"><svg width="18" height="14" viewBox="0 0 18 14"><path d="M9 13C5 11 2 8 1 3c4 1 7 4 8 10zm0 0c4-2 7-5 8-10-4 1-7 4-8 10z" fill="#3f8a1c"/></svg>Special Packages</h3>
    <div class="pkg-list" style="top:146px">
      <div class="pkg"><h5>SMALL PACKAGE #1</h5><p>30 minutes deep tissue body massage<br>15 minutes foot reflexology<br>30 minutes relaxing facial<br><span class="price">$105 (Regular Price: $125)</span></p></div>
      <div class="pkg"><h5>SMALL PACKAGE #2</h5><p>30 minutes hot stone body massage<br>30 minutes paraffin hand treatment<br><span class="price">$75 (Regular Price: $90)</span></p></div>
      <div class="pkg"><h5>LARGE PACKAGE #3</h5><p>60 minutes deep tissue body massage<br>15 minutes foot reflexology<br>30 minutes hot stone therapy<br>30 minutes paraffin hand treatment<br><span class="price">$180 (Regular Price: $220)</span></p></div>
    </div>
    <h3 class="pkg-heading" style="top:432px"><svg width="18" height="14" viewBox="0 0 18 14"><path d="M9 13C5 11 2 8 1 3c4 1 7 4 8 10zm0 0c4-2 7-5 8-10-4 1-7 4-8 10z" fill="#3f8a1c"/></svg>SPA Packages</h3>
    <div class="pkg-list" style="top:458px">
      <div class="pkg"><h5>SPA PACKAGE A</h5><p>30 minutes pure glow facial<br>Facial + body massage<br>Paraffin wax hand treatment<br><span class="price">$110 (Regular Price: $135)</span></p></div>
      <div class="pkg"><h5>SPA PACKAGE B</h5><p>60 minutes pure glow facial<br>60 minutes full body massage<br>30 minutes foot reflexology<br>Paraffin wax hand treatment<br><span class="price">$165 (Regular Price: $200)</span></p></div>
    </div>
    <div class="pkg-bottom" role="img" aria-label="Photo of green spa oils and leaves"></div>
  </section>

  <section class="panel panel-front">
    <div class="front-photo" role="img" aria-label="Close-up photo of a green leaf covered in water droplets"></div>
    <div class="brand"><span class="dot"></span>CALMIVERA</div>
    <p class="slogan script">Come to where your stress melts away</p>
    <p class="web">www.calmiverahealth.example</p>
  </section>
</main>

<div class="board-label label-back">Back</div>
<div class="board-label label-front">Front</div>
</body>
</html>
```